Vegan Chinese & Malaysian Restaurant in Australia Needs a Refreshed Menu Design

We are currently looking to update our menu with a refreshed modern Asian (authenticity matters, no hints of cultural appropriation or stereotyping) look that is more vibrant, easy to read compared to the current menu (attached).
The new menu will be split into 2 sets:
a) Menu for savoury dishes
b) Drinks and sweets menu

Target Market(s)

Our target audience is a blend of moderately late 20s to 40s moderately affluent singles, couples and families, and younger millennial foodies who love plant based food.

Industry/Entity Type

Restaurant

Font styles to use
Serif
Sans Serif
Other font styles liked:
• Please view mood board attached

Requirements
Must have
• Include most or all of the attached images (feel free to edit them) in a creative yet professional way. Follow guidance and inspo on mood board attached - including brand colours. Look like a noticeable refresh from the previous menu version. The design can be done to suit a full bleed print for supporting any visual elements. However, please ensure text is kept to conventional A4 safe area printing.
Nice to have
• Good readability - reader must be able to read starting from top left corner (like a book).
Should not have
• Colours other than those specified in the mood board. More than 3 fonts. Currency signs on prices.

```html
<!DOCTYPE html>
<html lang="en">
<head>
<meta charset="utf-8">
<title>Jade Table – Yum Cha Menu</title>
<link rel="stylesheet" href="https://fonts.googleapis.com/css2?family=Poppins:wght@400;500;600;700;800&display=swap">
<style>
  :root {
    --backdrop: #66b266;
    --paper: #e6e6e4;
    --ink: #4a4a4a;
    --rule: #7a7a7a;
    --brand-green: #5a9a58;
    --deep-green: #27492a;
    --cover-light: #c4c8c7;
    --cover-dark: #586361;
    --badge: #8fb88a;
    --plate: #d9d6d1;
    --glaze: #7a3d1e;
    --white: #ffffff;
  }
  * { box-sizing: border-box; margin: 0; padding: 0; }
  html, body { width: 1200px; height: 800px; overflow: hidden; }
  body {
    background: var(--backdrop);
    font-family: "Poppins", sans-serif;
    color: var(--ink);
    display: flex;
    align-items: center;
    justify-content: center;
  }
  .spread { display: flex; width: 1040px; height: 735px; box-shadow: 0 8px 24px rgba(0,0,0,.18); }
  .page { position: relative; width: 520px; height: 735px; overflow: hidden; }

  /* Inside page */
  .page--menu { background: var(--paper); }
  .dish-photo {
    position: absolute; right: 0; top: 0; width: 190px; height: 480px;
    background:
      radial-gradient(ellipse 70% 45% at 55% 40%, var(--glaze) 0 60%, transparent 62%),
      linear-gradient(180deg, #dcd8d2 0%, var(--plate) 60%, var(--paper) 100%);
  }
  .brush-mark {
    position: absolute; right: -70px; top: 470px; width: 240px; height: 240px;
    border-radius: 50%; background: var(--deep-green);
  }
  .menu-column { position: absolute; left: 36px; top: 38px; width: 272px; }
  .menu-title {
    display: flex; align-items: center; gap: 8px;
    color: var(--brand-green); font-weight: 800; font-size: 26px; letter-spacing: .5px;
    margin-bottom: 12px;
  }
  .menu-title::before { content: ""; width: 40px; height: 3px; background: var(--brand-green); }
  .menu-section { margin-bottom: 9px; }
  .section-title { color: var(--brand-green); font-weight: 700; font-size: 13px; margin-bottom: 3px; }
  .dish { border-bottom: 1px dashed var(--rule); padding: 3px 0 4px; }
  .dish:last-child { border-bottom: none; }
  .dish-name { font-weight: 600; font-size: 10px; line-height: 1.3; }
  .dish-desc { font-weight: 400; font-size: 9.5px; line-height: 1.3; }

  /* Cover */
  .page--cover { background: linear-gradient(100deg, var(--cover-light) 0%, #8e9694 45%, var(--cover-dark) 100%); }
  .brand-badge {
    position: absolute; left: 200px; top: 40px; width: 240px; height: 240px;
    border-radius: 50%; background: var(--badge);
    display: flex; align-items: center; justify-content: center;
  }
  .brand-name {
    color: var(--white); font-weight: 500; font-size: 40px; line-height: 1.05; text-align: center;
  }
  .soup-photo {
    position: absolute; left: -140px; top: 390px; width: 600px; height: 600px;
    border-radius: 50%; border: 10px solid #dfe3e0;
    background: radial-gradient(circle at 50% 40%, #d9a36c 0 35%, #b97a45 55%, #8c5d3a 70%);
  }
</style>
</head>
<body>
  <main class="spread">
    <section class="page page--menu">
      <div class="dish-photo" role="img" aria-label="Photo of glazed sesame tofu pieces on noodles"></div>
      <div class="brush-mark" role="img" aria-label="Dark green ink brush stroke"></div>

      <div class="menu-column">
        <h1 class="menu-title">YUM CHA</h1>

        <div class="menu-section">
          <h2 class="section-title">Love Buns</h2>
          <div class="dish"><p class="dish-name">BBQ ‘Pork’ Bun</p>
            <p class="dish-desc">Australian unbleaches wheat &amp; rye flour buns filled with our chunky bbq ‘pork’ fermented hoisin sauce (2 pieces) 6</p></div>
          <div class="dish"><p class="dish-name">Spicy Eggplant Bun</p>
            <p class="dish-desc">Aust eggplant stewed in a Beijing-style chilli ( mild ) with chickpeas ; encased in a fluffy paprika bun pastry ( 2 pieces ) 6</p></div>
        </div>

        <div class="menu-section">
          <h2 class="section-title">Dumplings &amp; Buns</h2>
          <div class="dish"><p class="dish-name">Steamed Dim Sims</p>
            <p class="dish-desc">Marinated shiitak mushrooms, tender Australian soy mince with a colorful vegetable medley, wrapped in a thin silky pastry ( 3 pieces ) 7.5</p></div>
          <div class="dish"><p class="dish-name">Steamed Vegetable Rolls</p>
            <p class="dish-desc">Julienne rainbow vegetables wrapped in fresh tofu sheets ( 2 pieces ) 7.5</p></div>
          <div class="dish"><p class="dish-name">Spinach Chia Dumplings</p>
            <p class="dish-desc">Fresh Australian spinach work-fried with seasonal vegetables and ginger in spinach juice infused chia seed pastry ( 3 pieces ) 7.5</p></div>
          <div class="dish"><p class="dish-name">Chia ‘ Prawn ’ Dumplings</p>
            <p class="dish-desc">Faux ‘prawn’ crunchy water chestnut, tender bamboo shoots and fresh crushed ginger, wrapped in tumeric infused chia seed pastry ( 3 pieces ) 7.5</p></div>
        </div>

        <div class="menu-section">
          <h2 class="section-title">From the Wok / Air Fryer</h2>
          <div class="dish"><p class="dish-name">Spring Rolls</p>
            <p class="dish-desc">3 ( pieces ) 6.5</p></div>
          <div class="dish"><p class="dish-name">New ‘Duck’ Spring Rolls</p>
            <p class="dish-desc">The first vegan ones in Sydney! ( 3 pieces ) 8</p></div>
          <div class="dish"><p class="dish-name">Crispy Seaweed Rolls</p>
            <p class="dish-desc">Lightly battered and wrapped around sautted julienne vegetables and shitake mushroom ( 3 pieces ) 7.5</p></div>
          <div class="dish"><p class="dish-name">Crispy &amp; Fluffy Tofu Layers</p>
            <p class="dish-desc">Marinated for 12 hours in our chinese spice blend 7.5</p></div>
        </div>
      </div>
    </section>

    <section class="page page--cover">
      <div class="brand-badge"><p class="brand-name">Jade<br>Table</p></div>
      <div class="soup-photo" role="img" aria-label="Photo of a bowl of laksa soup with broccoli, tofu and vegan prawns"></div>
    </section>
  </main>
</body>
</html>
```